Tonic und Gin Tonic
Zielgruppe
Von Brennhof in alle Welt
Heute arbeiten über 65 Mitarbeiter aus der Region. Auf 30.000 Quadratmetern werden täglich 200.000 Flaschen Hochprozentiges produziert und abgefüllt. Weitere Produktionsflächen auf 85.000 Quadratmetern in Polen dienen ebenfalls der Unternehmensaktivität Mit einer Produktion von mehr als 30 Millionen Flaschen im Jahr ist die Brennhofer Destillerie heute einer der größten Spirituosenhersteller Deutschlands. Und in der Tat könnte man sich hier verlaufen. Die Lagerkapazität reicht für zwei Millionen Flaschen. Die Getränkeauswahl ist immens. Die Produktion erfolgt auf acht automatisierten Abfülllinien. Die Brennhofer Spezialitäten werden ins In- und Ausland verschickt. Nach Israel, nach China und Amerika – die Liste ist lang. „Wir haben mehr als 120 verschiedene Produkte im Programm, Frucht- und Sahneliköre, Klare und Kräuterschnäpse“.
Neben Glas und PET fertigen wir Dosen in 200 ml, 250 ml slim, 330 ml und 500 ml.
Aufgabenstellung
Kreativ, einzigartig, ansprechend, marktkonform und realistisch, keine Kunst! Da wir bereits mit nationalen und internationalen Firmen zusammenarbeiten, auch Polen, Bulgarien und Rumänien kennen wir die Preislage bezüglich Design und Entwicklung und suchen einen Partner / Designer, mehr Leistung erbringen kann als versprochen wird.
Bei Interesse streben wir eine langfristige Zusammenarbeit an.
Im Anhang finden Sie Bildmaterial, was von einem anderen Produkt stammt mit Copyright!. Es geht be der Entwicklung um eine Dose von 250 ml Slim.
Es geht um die Entwicklung eines Design für ein neues Dosengetränk. Weitere Feinheiten und Einzelheiten per Telefon und oder Email.

```html
<!DOCTYPE html>
<html lang="de">
<head>
<meta charset="utf-8">
<title>Yuzu Tonic – Verpackungsdesign Version A</title>
<link rel="stylesheet" href="https://fonts.googleapis.com/css2?family=Archivo:wght@500;800&family=Barlow:wght@300;400&family=Roboto+Condensed:wght@300;400&display=swap">
<style>
  :root {
    --page-bg: #ffffff;
    --ink: #111111;
    --accent: #f5c542;
    --label-bg: #d9eded;
    --label-line: #f3efdc;
    --label-edge: #8a9a9a;
    --text-soft: #8fa3a3;
    --text-strong: #7a9191;
    --slice-rind: #f6dc86;
    --slice-flesh: #f3e7c4;
    --slice-core: #fdfaee;
  }
  * { margin: 0; padding: 0; box-sizing: border-box; }
  html, body {
    width: 800px; height: 1200px; overflow: hidden;
    background: var(--page-bg);
  }
  .canvas { position: relative; width: 800px; height: 1200px; }

  /* Page header */
  .page-title {
    position: absolute; left: 92px; top: 140px;
    font-family: "Barlow", sans-serif; font-weight: 300;
    font-size: 44px; line-height: 55px; letter-spacing: 0.01em;
    color: var(--ink);
  }
  .version-marker {
    position: absolute; left: 52px; top: 264px;
    font-family: "Barlow", sans-serif; font-weight: 400;
    font-size: 26px; line-height: 30px; color: var(--accent);
  }
  .version-title {
    position: absolute; left: 92px; top: 272px;
    font-family: "Barlow", sans-serif; font-weight: 300;
    font-size: 31px; line-height: 38px; color: var(--ink);
  }
  .page-intro {
    position: absolute; left: 93px; top: 331px;
    font-family: "Barlow", sans-serif; font-weight: 300;
    font-size: 10.5px; line-height: 15px; color: var(--ink);
  }
  .page-footer {
    position: absolute; right: 54px; top: 1145px;
    font-family: "Barlow", sans-serif; font-weight: 400;
    font-size: 9px; color: var(--ink);
  }

  /* Can label */
  .label {
    position: absolute; left: 70px; top: 619px;
    width: 661px; height: 463px;
    border: 1px solid var(--label-edge);
    box-shadow: 2px 3px 4px rgba(0,0,0,0.18);
    overflow: hidden;
  }
  .label-pattern {
    position: absolute; inset: 0;
    background:
      radial-gradient(circle at 64% 36%, var(--label-line) 0%, rgba(243,239,220,0.35) 30%, var(--label-bg) 70%),
      var(--label-bg);
  }
  .info {
    position: absolute; left: 23px; width: 146px;
    font-family: "Roboto Condensed", sans-serif; font-weight: 300;
    color: var(--text-soft); font-size: 7.2px; line-height: 9.9px;
    white-space: nowrap;
  }
  .info-heading {
    font-family: "Archivo", sans-serif; font-weight: 500;
    font-size: 8px; letter-spacing: 0.08em; text-align: center;
    line-height: 10px;
  }
  .info-center { text-align: center; }
  .nutrition { width: 100%; border-collapse: collapse; }
  .nutrition td { padding: 0; line-height: 9.9px; white-space: nowrap; }
  .nutrition td:last-child { text-align: right; }
  .indent { padding-left: 9px; }
  .volume {
    position: absolute; left: 120px; top: 426px; width: 49px;
    font-family: "Roboto Condensed", sans-serif; font-weight: 400;
    color: var(--text-soft); font-size: 14px; text-align: right;
  }
  .yuzu-slice {
    position: absolute; left: 344px; top: 88px;
    width: 154px; height: 154px; border-radius: 50%;
    background: radial-gradient(circle, var(--slice-core) 0%, var(--slice-flesh) 55%, var(--slice-flesh) 88%, var(--slice-rind) 92%);
  }
  .brand {
    position: absolute; left: 321px; width: 200px; text-align: center;
    font-family: "Archivo", sans-serif; font-weight: 800;
    color: var(--text-strong);
  }
  .brand-name { top: 288px; font-size: 27px; letter-spacing: 0.2em; padding-left: 0.2em; }
  .brand-type { top: 326px; font-size: 14px; letter-spacing: 0.16em; padding-left: 0.16em; }
</style>
</head>
<body>
<main class="canvas">
  <h1 class="page-title">Simplistic<br>Illustration</h1>
  <span class="version-marker" aria-hidden="true">»</span>
  <h2 class="version-title">Version A</h2>
  <p class="page-intro">Frischer Geschmack, der sich im Mund ausbreitet<br>mit jedem Schluck des neuen Yuzu Tonics.</p>

  <section class="label">
    <div class="label-pattern" role="img" aria-label="Feines Muster aus cremefarbenen Wellenlinien, die sich ringförmig um die Yuzu-Scheibe auf hellblauem Grund ausbreiten"></div>

    <div class="info" style="top:28px">
      <p class="info-heading">CHININHALTIGES<br>ERFRISCHUNGSGETRÄNK</p>
      <p class="info-center">mit Yuzusaft; Saftgehalt mindestens: 2,3 %</p>
    </div>
    <div class="info" style="top:74px">
      <p class="info-heading" style="margin-bottom:4px">ZUTATEN</p>
      <p>Wasser, Zucker, Yuzusaft (2,3 %), Kohlensäure,<br>Säurungsmittel: Citronensäure (oder E330),<br>Aroma, Chinin.</p>
    </div>
    <div class="info" style="top:134px">
      <p class="info-heading" style="margin-bottom:5px">NÄHRWERTKENNZEICHNUNG</p>
      <p class="info-center" style="margin-bottom:5px">Ø Nährwerte</p>
      <p class="info-center" style="margin-bottom:5px; padding-left:10px">pro 100 ml | pro Portion (250 ml)** | % RM***</p>
      <table class="nutrition">
        <tr><td>Brennwert (kJ/kcal)</td><td>147/35 | 368/87 | 4%</td></tr>
        <tr><td>Fett (g)</td><td>0,0 | 0,0 | 0%</td></tr>
        <tr><td>davon gesättigte Fettsäuren (g)</td><td>0,0 | 0,0 | 0%</td></tr>
        <tr><td>Kohlenhydrate (g)</td><td>8,4 | 21,0 | 8%</td></tr>
        <tr><td>davon Zucker (g)</td><td>8,4 | 21,0 | 23%</td></tr>
        <tr><td>Eiweiß (g)</td><td>0,0 | 0,0 | 0%</td></tr>
        <tr><td>Salz (g)</td><td>0,000 | 0,0 | 0%</td></tr>
      </table>
    </div>
    <div class="info" style="top:264px">
      <p style="margin-bottom:5px">** Die Packung enthält x-Portionen<br><span class="indent">(abhängig von Gebinde- und Portionsgröße)</span></p>
      <p style="margin-bottom:5px">*** RM=Referenzmenge für einen durchschnitt-<br><span class="indent">lichen Erwachsenen (8400kJ/2000 kcal)</span></p>
      <p style="margin-bottom:5px">Berechnung aus Literaturdaten</p>
      <p>der Salzgehalt bezieht sich auf die Verwendung<br>von entmineralisiertem Wasser</p>
    </div>
    <div class="info" style="top:364px">
      <p class="info-heading" style="margin-bottom:5px">MINDESTENS HALTBAR BIS</p>
      <p style="margin-bottom:5px">-Tag/Monat/Jahr-</p>
      <p>Name und Anschrift des<br>Lebensmittelherstellers oder Importeur</p>
    </div>

    <p class="volume">250ml</p>

    <div class="yuzu-slice" role="img" aria-label="Illustration einer aufgeschnittenen Yuzu-Scheibe mit gelber Schale und hellen Fruchtsegmenten"></div>

    <p class="brand brand-name">YUZU</p>
    <p class="brand brand-type">TONIC</p>
  </section>

  <p class="page-footer">Brennhof Yuzu Tonic Packaging Design ·&nbsp; Page 3</p>
</main>
</body>
</html>
```